Cutting Board Oil Label

I would like a label created for our custom made cutting board oil. The bottle will be clear and come in several different sizes. I have included the current label we use. We would like the information to stay the same, but more aesthetically pleasing and professionally presented. I am also including our logo and the current label of our biggest competitor.

```html
<!DOCTYPE html>
<html lang="en">
<head>
<meta charset="utf-8">
<title>Cutting Board Conditioner Label</title>
<link href="https://fonts.googleapis.com/css2?family=Berkshire+Swash&family=Roboto+Condensed:wght@300;400;700&display=swap" rel="stylesheet">
<style>
  :root {
    --page: #f4f4f4;
    --white: #ffffff;
    --teal: #45c3cf;
    --teal-deep: #2fb4c2;
    --sand: #ecd09b;
    --ink: #111111;
    --grey: #6b6b6b;
    --brand-teal: #2ab7c6;
  }
  * { box-sizing: border-box; margin: 0; padding: 0; }
  html, body { width: 1200px; height: 1200px; overflow: hidden; background: var(--page); }
  .canvas {
    width: 1200px; height: 1200px;
    display: flex; align-items: center; justify-content: center;
  }
  .label {
    width: 590px; height: 1120px;
    border-radius: 42px;
    overflow: hidden;
    background: var(--white);
    display: flex; flex-direction: column;
    box-shadow: 0 4px 14px rgba(0,0,0,0.18);
    font-family: "Roboto Condensed", sans-serif;
    color: var(--ink);
  }
  .brand {
    height: 289px;
    display: flex; flex-direction: column; align-items: center; justify-content: center;
    gap: 14px;
  }
  .brand-mark {
    width: 64px; height: 64px; border-radius: 50%;
    background: var(--brand-teal);
  }
  .brand-name {
    font-family: "Roboto Condensed", sans-serif;
    font-weight: 400;
    font-size: 46px;
    color: var(--grey);
    letter-spacing: 0.5px;
  }
  .rule { height: 18px; background: var(--sand); }
  .product {
    height: 298px;
    background: var(--teal);
    display: flex; flex-direction: column; align-items: center; justify-content: center;
    text-align: center;
  }
  .product-title {
    font-family: "Berkshire Swash", cursive;
    font-weight: 400;
    font-size: 84px;
    line-height: 96px;
    color: var(--white);
    margin-top: 8px;
  }
  .product-use {
    font-weight: 300;
    font-size: 27px;
    line-height: 38px;
    margin-top: 6px;
    color: var(--ink);
  }
  .claims {
    height: 156px;
    background: var(--sand);
    display: flex; flex-direction: column; align-items: center; justify-content: center;
    text-align: center;
  }
  .claims-headline { font-weight: 700; font-size: 46px; line-height: 52px; }
  .claims-label { font-weight: 300; font-size: 22px; line-height: 30px; margin-top: 6px; }
  .claims-ingredients { font-weight: 300; font-size: 22px; line-height: 30px; }
  .usage {
    height: 359px;
    background: var(--teal);
    padding: 29px 16px 0;
    display: flex; flex-direction: column;
  }
  .directions {
    border: 3px solid var(--ink);
    border-radius: 22px;
    overflow: hidden;
    background: var(--white);
  }
  .directions-heading {
    background: var(--ink);
    color: var(--white);
    font-weight: 700;
    font-size: 34px;
    line-height: 42px;
    text-align: center;
  }
  .directions-body {
    padding: 10px 16px 12px;
    font-weight: 300;
    font-size: 19.5px;
    line-height: 25.5px;
    text-align: justify;
  }
  .footer {
    display: flex; justify-content: space-between;
    padding: 12px 6px 0;
    font-weight: 700;
    font-size: 24px;
    color: var(--ink);
  }
</style>
</head>
<body>
<main class="canvas">
  <article class="label">
    <header class="brand">
      <span class="brand-mark"></span>
      <span class="brand-name">Laurel Hollow Gifts</span>
    </header>
    <div class="rule"></div>
    <section class="product" role="img" aria-label="Teal wood-grain texture band behind the product name">
      <h1 class="product-title">Cutting Board<br>Conditioner</h1>
      <p class="product-use">For use on cutting boards, butcher blocks,<br>wood utensils, and any other wood products.</p>
    </section>
    <section class="claims">
      <h2 class="claims-headline">FOOD SAFE - ALL NATURAL</h2>
      <p class="claims-label">Made with:</p>
      <p class="claims-ingredients">Beeswax, Mineral Oil,Orange Oil, Lemon Oil, and Vitamin E</p>
    </section>
    <section class="usage" role="img" aria-label="Teal wood-grain texture band behind the directions">
      <div class="directions">
        <h3 class="directions-heading">DIRECTIONS:</h3>
        <p class="directions-body">Apply a generous amount of conditioner with a clean, lint free cloth. For best results, allow board to soak in conditioner overnight. Using a clean, lint free cloth, buff and remove any excess conditioner. For new or unconditioned cutting boards, butcher blocks, or wooden kitchen utensils we recommend repeating the process a second time to ensure your wood is properly sealed. Recondition about once a month (depending on frequency of use) or when the board begins to become dry to the touch.</p>
      </div>
      <footer class="footer">
        <span class="origin">Made in the USA</span>
        <span class="website">www.LaurelHollowGifts.com</span>
      </footer>
    </section>
  </article>
</main>
</body>
</html>
```